What makes us Different Managed Communications Services Provider Flyer

We need a flyer to explain why we are different than other "managed IT services" company. Gives a brief description of our company and services that can entice clients and potential clients to setup a FREE consultation with us. This will become part of an ongoing marketing campaign that includes emails, leave behinds, brochures, and more

```html
<!DOCTYPE html>
<html lang="en">
<head>
<meta charset="utf-8">
<title>Managed IT Provider Flyer</title>
<link rel="stylesheet" href="https://fonts.googleapis.com/css2?family=Open+Sans:ital,wght@0,400;0,600;0,700;1,400&family=Roboto:wght@500;700;900&display=swap">
<style>
  :root{
    --backdrop:#6a6a6a;
    --paper:#ffffff;
    --navy:#0a2f6b;
    --royal:#0d57a8;
    --sky:#1fb0e2;
    --sky-deep:#1590c9;
    --ink:#2c3440;
    --photo-a:#dfe6ee;
    --photo-b:#b9c6d4;
  }
  *{margin:0;padding:0;box-sizing:border-box}
  html,body{width:900px;height:1200px;overflow:hidden;background:var(--backdrop)}
  .flyer{position:absolute;left:35px;top:13px;width:830px;height:1174px;background:var(--paper);overflow:hidden;font-family:"Open Sans",Arial,sans-serif;color:var(--ink)}
  .hero-photo{position:absolute;left:438px;top:40px;width:392px;height:410px;background:linear-gradient(160deg,var(--photo-a),var(--photo-b) 60%,#f4f7fa)}
  .roof{position:absolute;left:0;top:0;width:830px;height:560px}
  .title{position:absolute;left:62px;top:78px;font-family:"Roboto",Arial,sans-serif;color:var(--navy);line-height:1}
  .title .kicker{font-size:20px;font-weight:500}
  .title .big{font-size:38px;font-weight:900;letter-spacing:.5px;margin-top:4px}
  .title .big.accent{color:var(--sky-deep)}
  .title .sub{font-size:22px;font-weight:700;margin-top:6px}
  .brand{position:absolute;left:520px;top:78px;display:flex;align-items:center;gap:10px;font-family:"Roboto",Arial,sans-serif;font-weight:700;font-size:22px;color:var(--royal)}
  .brand .mark{width:18px;height:18px;background:var(--sky)}
  .intro-box{position:absolute;left:60px;top:222px;width:335px;height:270px;background:var(--royal);color:#fff;font-size:12px;line-height:1.42;padding:20px 20px;text-align:justify}
  .clients-head{position:absolute;left:438px;top:452px;font-family:"Roboto",Arial,sans-serif;font-weight:700;font-size:26px;line-height:1.05;color:var(--royal)}
  .clients-head .lite{color:var(--sky)}
  .copy{position:absolute;font-size:11.8px;line-height:1.42;color:var(--ink)}
  .copy p+p{margin-top:10px}
  .copy b{font-weight:700;color:var(--navy)}
  .col-right{left:438px;width:365px}
  .col-left{left:40px;width:372px}
  .section-bar{position:absolute;height:26px;background:var(--sky-deep);color:#fff;font-family:"Roboto",Arial,sans-serif;font-weight:700;font-size:16px;line-height:26px;padding-left:22px}
  .section-bar::before{content:"";position:absolute;left:0;top:0;width:10px;height:26px;background:var(--navy)}
  .services{position:absolute;left:40px;top:925px;width:380px;display:grid;grid-template-columns:1fr 1fr;gap:16px 16px;font-size:11.2px;line-height:1.36}
  .service{display:flex;gap:8px;align-items:flex-start}
  .service svg{flex:none;width:24px;height:24px}
  .quote{position:absolute;left:438px;top:915px;width:370px;font-size:12px;line-height:1.45;padding:4px 34px 0 38px}
  .quote .qm{position:absolute;font-family:"Roboto",Arial,sans-serif;font-weight:900;font-size:50px;color:var(--royal);line-height:1}
  .quote .open{left:0;top:-6px}
  .quote .close{right:0;bottom:-30px}
  .site{position:absolute;left:0;width:830px;top:1104px;text-align:center;font-family:"Roboto",Arial,sans-serif;font-weight:500;font-size:18px;color:var(--navy)}
  .site-rule{position:absolute;left:300px;top:1134px;width:230px;height:2px;background:var(--navy)}
</style>
</head>
<body>
<div class="flyer">
  <div class="hero-photo" role="img" aria-label="Photo of a smiling man in a light shirt holding a small network device, office background"></div>

  <svg class="roof" viewBox="0 0 830 560" aria-hidden="true">
    <polygon points="300,380 420,300 830,440 830,472 420,334 300,414" fill="var(--sky)"/>
    <polygon points="420,295 830,434 830,444 420,305" fill="var(--royal)"/>
    <polygon points="395,492 395,522 340,492" fill="var(--navy)"/>
  </svg>

  <div class="title">
    <div class="kicker">More Than Just a</div>
    <div class="big accent">MANAGED</div>
    <div class="big">IT PROVIDER</div>
    <div class="sub">Our Legacy of Excellence</div>
  </div>

  <div class="brand"><span class="mark"></span>Northline Voice &amp; Data</div>

  <div class="intro-box">
    At our company, we are far more than your typical managed IT provider. Since our founding in 1983, we have built a reputation based on trust, reliability, and unparalleled service. With client relationships spanning 20 to 30 years, we have demonstrated a level of commitment that few IT firms can match. What sets us apart is not just our technical expertise but the deep, long-term partnerships we cultivate with our clients—many of whom have stayed with us without ever being locked into a contract. That is a testament to the exceptional quality of our service and the trust we have earned over decades.
  </div>

  <h2 class="clients-head"><span class="lite">OUR CLIENTS</span> STAY<br>BECAUSE WE DELIVER</h2>

  <div class="copy col-right" style="top:522px">
    <p>For over 40 years, we have maintained a standard of excellence that <b>other companies simply cannot compare with.</b> Our team of experts consistently goes above and beyond, ensuring that clients not only <b>get the support they need but also receive the strategic guidance necessary to stay ahead in an ever-evolving digital landscape.</b></p>
    <p>Our <b>90-day performance</b> review process ensures that we continuously improve our service based on client feedback. This process allows us to <b>adapt, refine, and enhance our approach,</b> providing a truly personalized IT experience that aligns with business objectives.</p>
  </div>

  <div class="section-bar" style="left:438px;top:748px;width:300px">A Legacy of Trust &amp; Reliability</div>
  <div class="copy col-right" style="top:786px">
    <p>The fact that many of our clients have remained with us for decades without a formal contract speaks volumes about the trust we have built. We don't lock in clients with paperwork—we keep them with results. <b>That's the difference between a standard managed IT provider and an IT partner who genuinely cares.</b></p>
  </div>

  <div class="quote">
    <span class="qm open">&ldquo;</span>
    If you're looking for an IT provider that will treat your business as if it were their own, look no further. Our legacy of service, innovation, and commitment to our clients is what sets us apart from the rest.
    <span class="qm close">&rdquo;</span>
  </div>

  <div class="section-bar" style="left:20px;top:598px;width:345px">A Commitment Beyond Contracts</div>
  <div class="copy col-left" style="top:636px">
    <p>Unlike many managed IT providers who rely on rigid contracts to retain clients, we believe that service excellence speaks for itself. The longevity of our client relationships is rooted in our ability to <b>anticipate needs, resolve challenges before they escalate, and proactively enhance network &amp; communication infrastructures. Our comprehensive checklists, questionnaires, policies, and procedures, attention to details ensure that every client receives a tailored, best-in-class experience from day one.</b></p>
  </div>

  <div class="section-bar" style="left:20px;top:822px;width:375px">A Holistic Approach to IT Management</div>
  <div class="copy col-left" style="top:858px">
    <p>We don't just manage IT—we integrate ourselves into your business, ensuring that technology aligns with your strategic goals. Our services go beyond traditional break-fix support; we offer:</p>
  </div>

  <div class="services">
    <div class="service">
      <svg viewBox="0 0 26 26" aria-hidden="true"><rect x="2" y="2" width="22" height="22" rx="4" fill="none" stroke="var(--royal)" stroke-width="2"/><path d="M7 18 L11 12 L15 15 L20 8" fill="none" stroke="var(--sky)" stroke-width="2"/></svg>
      <span>Strategic IT Roadmaps customized to drive business growth.</span>
    </div>
    <div class="service">
      <svg viewBox="0 0 26 26" aria-hidden="true"><rect x="2" y="2" width="22" height="22" rx="4" fill="none" stroke="var(--royal)" stroke-width="2"/><ellipse cx="13" cy="9" rx="6" ry="2.5" fill="none" stroke="var(--sky)" stroke-width="2"/><path d="M7 9 V17 C7 20 19 20 19 17 V9" fill="none" stroke="var(--sky)" stroke-width="2"/></svg>
      <span>Comprehensive backup and disaster recovery solutions that provide peace of mind.</span>
    </div>
    <div class="service">
      <svg viewBox="0 0 26 26" aria-hidden="true"><rect x="2" y="2" width="22" height="22" rx="4" fill="none" stroke="var(--royal)" stroke-width="2"/><path d="M13 6 L19 8.5 V13 C19 17 16 19.5 13 20.5 C10 19.5 7 17 7 13 V8.5 Z" fill="none" stroke="var(--sky)" stroke-width="2"/></svg>
      <span>Proactive cybersecurity assessments that help keep businesses secure.</span>
    </div>
    <div class="service">
      <svg viewBox="0 0 26 26" aria-hidden="true"><rect x="2" y="2" width="22" height="22" rx="4" fill="none" stroke="var(--royal)" stroke-width="2"/><circle cx="13" cy="13" r="6" fill="none" stroke="var(--sky)" stroke-width="2"/><path d="M13 9.5 V13 L15.5 14.5" fill="none" stroke="var(--sky)" stroke-width="2"/></svg>
      <span>Industry-leading response times and dedicated support teams focused on delivering an exceptional client experience.</span>
    </div>
  </div>

  <div class="site">www.northlinevoice.com</div>
  <div class="site-rule"></div>
</div>
</body>
</html>
```